E-commerce Website needs category banner

What we need for our category banner is a clean, predominately black design that showcases the product we are trying to sell (currently only 1), and a few subtle gradients that follow the pattern set by previous designs.

An example will be provided to showcase what we want.

It needs to say:
Outdoor Motion Detection Lighting in large, clear font similar to the example provided.

Please ensure dimensions are as follows: 980x300

Target Market(s)

Senior citizens, businesses, homeowners, families, etc

Industry/Entity Type

Product

Font styles to use
Sans Serif

Requirements
Must have
• It needs to say:
Outdoor Motion Detection Lighting in large, clear font similar to the example provided
980x300 is the required size!
Should not have
• Too much going on- clean and simple please (no crazy fonts, logos, etc)

```html
<!DOCTYPE html>
<html lang="en">
<head>
<meta charset="utf-8">
<title>Outdoor Motion Detection Lighting – Category Banners</title>
<link rel="stylesheet" href="https://fonts.googleapis.com/css2?family=Archivo:wdth,wght@62..125,800..900&display=swap">
<style>
  :root {
    --page-bg: #ffffff;
    --text-light: #ffffff;
    --charcoal-edge: #1c1c1c;
    --charcoal-mid: #2a2a2a;
    --charcoal-glow: #474747;
    --sky: #97cbe6;
    --sky-glow: #f4f8fa;
    --peach: #efb39a;
    --peach-glow: #fbf1ed;
    --product-light: rgba(240, 240, 240, 0.85);
    --product-shade: rgba(215, 215, 215, 0.35);
  }
  * { box-sizing: border-box; margin: 0; padding: 0; }
  html, body {
    width: 1200px;
    height: 1000px;
    overflow: hidden;
    background: var(--page-bg);
  }
  .banner-stack {
    position: absolute;
    left: 207px;
    top: 36px;
    width: 784px;
    display: flex;
    flex-direction: column;
    gap: 8px;
  }
  .banner {
    position: relative;
    width: 784px;
    height: 304px;
    overflow: hidden;
  }
  .banner--charcoal {
    background: radial-gradient(ellipse 330px 250px at 78% 50%, var(--charcoal-glow), var(--charcoal-mid) 60%, var(--charcoal-edge));
  }
  .banner--sky {
    background: radial-gradient(circle 200px at 78% 55%, var(--sky-glow) 30%, var(--sky) 100%), var(--sky);
  }
  .banner--peach {
    background: radial-gradient(circle 200px at 78% 55%, var(--peach-glow) 30%, var(--peach) 100%), var(--peach);
  }
  .banner__title {
    position: absolute;
    left: 57px;
    top: 50px;
    font-family: "Archivo", "Arial Black", sans-serif;
    font-weight: 900;
    font-stretch: 88%;
    font-variation-settings: "wdth" 88;
    font-size: 54px;
    line-height: 53.6px;
    letter-spacing: -1.2px;
    color: var(--text-light);
    text-transform: uppercase;
  }
  .banner__title span { display: block; }
  .banner__product {
    position: absolute;
    left: 460px;
    top: 50px;
    width: 260px;
    height: 210px;
    background: radial-gradient(ellipse at 55% 45%, var(--product-light) 0%, var(--product-shade) 45%, transparent 70%);
  }
</style>
</head>
<body>
  <main class="banner-stack">
    <section class="banner banner--charcoal">
      <h1 class="banner__title"><span>Outdoor</span><span>Motion</span><span>Detection</span><span>Lighting</span></h1>
      <div class="banner__product" role="img" aria-label="Two white wall-mounted motion sensor LED spotlights"></div>
    </section>
    <section class="banner banner--sky">
      <h2 class="banner__title"><span>Outdoor</span><span>Motion</span><span>Detection</span><span>Lighting</span></h2>
      <div class="banner__product" role="img" aria-label="Two white wall-mounted motion sensor LED spotlights"></div>
    </section>
    <section class="banner banner--peach">
      <h2 class="banner__title"><span>Outdoor</span><span>Motion</span><span>Detection</span><span>Lighting</span></h2>
      <div class="banner__product" role="img" aria-label="Two white wall-mounted motion sensor LED spotlights"></div>
    </section>
  </main>
</body>
</html>
```